Meadowlark Behavioral Partners, LLC Needs Modern Business Card Design.

We provide behavioral health services from western Kansas to eastern Kansas. There is an abundance of competition for the services we provide with our main competitor being larger and having significantly more financial resources; however, the quality of services we provide is greater and we have started to catch the attention of the State of Kansas. We had a great logo designed by PixelGuild - this will be used to build upon our brand. The logo (attached) should be used in the card development. We want something unique, modern, but also a card design that clearly states our name, contact info, provides the name and unqiue location of each clinician, etc. Rounded edges, or a unique size, just something that makes our business card stand out from others. I have also uploaded each clinician's name and their unique location and phone number.

Our idea is to have one side be black with our logo. Then, on the other side have business cards for each individual. Plus, we want one card that is "generic" with no specific clinician's name listed so that we can give clients an appointment card when they leave. Some clinicians have two locations - we're open to design and background color, but we have started going with branding colors of black, the yellow in the logo files attached, and sometimes a gray. Our new office has been decorated using this theme.

Target Market(s)

individuals and families in need of behavioral health services; potential professional referral sources; existing referral sources

Industry/Entity Type

Business

Contact Information for Business Card

I attached a Word doc that provides clinician names, credentials and location information specific to each individual.

Font styles to use
Serif

Colors
000000
fbed22
dbdbdb
9d9d9d
c3c3c3

Requirements
Must have
• 1) use of the company logo that has been attached; 2) a template that provides us space to individualize business cards for all of our clinicians; 3) should stick to the colors we are branding with: black, yellow from the logo file, maybe a gray shade and we're open to a suggestion on a shade of white.
Nice to have
• Group discussion culminated in the thought that one side would be black with just our logo - no clinician names, etc. A unique design - rounded edges, unique size, some catchy lay-out would be nice.
Should not have
• Must not be too busy. Should look "clean." The project should stick to branding colors: black, yellow (from the logo file), maybe a gray and shade of white.

```html
<!DOCTYPE html>
<html lang="en">
<head>
<meta charset="UTF-8">
<title>Meadowlark Behavioral Partners — Business Card</title>
<link href="https://fonts.googleapis.com/css2?family=Lora:wght@400;600;700&display=swap" rel="stylesheet">
<style>
  :root {
    --backdrop: #2b2b2b;
    --card-black: #050505;
    --gold: #f5b916;
    --white: #ffffff;
    --text-light: #e6e6e6;
  }
  html, body {
    margin: 0;
    padding: 0;
    width: 1200px;
    height: 880px;
    overflow: hidden;
    background: var(--backdrop);
    font-family: "Lora", Georgia, serif;
  }
  .canvas {
    position: relative;
    width: 1200px;
    height: 880px;
  }
  .card {
    position: absolute;
    width: 620px;
    height: 354px;
    border-radius: 28px;
    overflow: hidden;
    background: var(--card-black);
    box-shadow: 0 14px 30px rgba(0,0,0,0.45);
  }
  .card-front { left: 90px; top: 70px; }
  .card-back { left: 490px; top: 456px; }

  /* Front side */
  .front-brand {
    position: absolute;
    inset: 0;
    display: flex;
    flex-direction: column;
    align-items: center;
    justify-content: center;
    text-align: center;
  }
  .brand-name {
    color: var(--gold);
    font-weight: 600;
    text-transform: uppercase;
    margin: 0;
    line-height: 1.1;
    white-space: nowrap;
  }
  .front-brand .brand-line-main { font-size: 46px; letter-spacing: 4px; }
  .front-brand .brand-line-sub { font-size: 18px; letter-spacing: 2px; margin-top: 6px; }
  .front-web {
    margin-top: 34px;
    color: var(--text-light);
    font-size: 15px;
    letter-spacing: 0.5px;
  }

  /* Back side */
  .back-shape {
    position: absolute;
    inset: 0;
    width: 620px;
    height: 354px;
  }
  .contact {
    position: absolute;
    left: 34px;
    top: 34px;
    color: var(--text-light);
    font-size: 13px;
    line-height: 1.4;
  }
  .person-name {
    color: var(--gold);
    font-size: 25px;
    font-weight: 700;
    margin: 0;
    line-height: 1.1;
  }
  .person-title { margin: 0 0 4px 0; font-size: 14px; }
  .person-email { margin: 0 0 12px 0; }
  .office { margin: 0 0 10px 0; }
  .office p { margin: 0; }
  .phone-row {
    display: flex;
    align-items: center;
    gap: 8px;
    margin-top: 3px;
  }
  .phone-icon { width: 18px; height: 18px; flex: none; }
  .back-brand {
    position: absolute;
    left: 452px;
    top: 128px;
    width: 160px;
    display: flex;
    flex-direction: column;
    align-items: center;
    text-align: center;
  }
  .back-brand .brand-line-main { font-size: 19px; letter-spacing: 1.5px; }
  .back-brand .brand-line-sub { font-size: 8.5px; letter-spacing: 0.3px; margin-top: 4px; }
</style>
</head>
<body>
<main class="canvas">

  <section class="card card-front" aria-label="Card front">
    <div class="front-brand">
      <p class="brand-name brand-line-main">Meadowlark</p>
      <p class="brand-name brand-line-sub">Behavioral Partners, LLC</p>
      <p class="front-web">www.meadowlarkbehavioral.com</p>
    </div>
  </section>

  <section class="card card-back" aria-label="Card back">
    <svg class="back-shape" viewBox="0 0 620 354" aria-hidden="true">
      <path d="M430 0 C405 150 470 290 580 354 L620 354 L620 0 Z" fill="var(--white)"/>
      <path d="M424 0 C399 150 464 292 572 354" fill="none" stroke="var(--gold)" stroke-width="4"/>
    </svg>

    <div class="contact">
      <h1 class="person-name">Daniel R. Holt, LCP</h1>
      <p class="person-title">President</p>
      <p class="person-email">dholt@meadowlarkbehavioral.com</p>

      <div class="office">
        <p>418 N. Elm St.</p>
        <p>Salina, Kansas 67401</p>
        <div class="phone-row">
          <svg class="phone-icon" viewBox="0 0 18 18" aria-hidden="true">
            <circle cx="9" cy="9" r="9" fill="var(--gold)"/>
            <path d="M6 4.5 L7.6 4.5 L8.3 6.8 L7.2 7.6 C7.7 8.9 8.9 10.1 10.3 10.7 L11.1 9.6 L13.4 10.3 L13.4 11.9 C13.4 12.5 12.9 13 12.3 13 C8.6 12.8 5.4 9.7 5.1 5.6 C5.1 5 5.5 4.5 6 4.5 Z" fill="var(--card-black)"/>
          </svg>
          <span>(555) 214-3360</span>
        </div>
      </div>

      <div class="office">
        <p>207 W. 9th St., Ste. 110</p>
        <p>Emporia, Kansas 66801</p>
        <div class="phone-row">
          <svg class="phone-icon" viewBox="0 0 18 18" aria-hidden="true">
            <circle cx="9" cy="9" r="9" fill="var(--gold)"/>
            <path d="M6 4.5 L7.6 4.5 L8.3 6.8 L7.2 7.6 C7.7 8.9 8.9 10.1 10.3 10.7 L11.1 9.6 L13.4 10.3 L13.4 11.9 C13.4 12.5 12.9 13 12.3 13 C8.6 12.8 5.4 9.7 5.1 5.6 C5.1 5 5.5 4.5 6 4.5 Z" fill="var(--card-black)"/>
          </svg>
          <span>(555) 830-1192</span>
        </div>
      </div>

      <div class="phone-row">
        <svg class="phone-icon" viewBox="0 0 18 18" aria-hidden="true">
          <circle cx="9" cy="9" r="9" fill="var(--gold)"/>
          <rect x="5" y="7" width="8" height="6" rx="1" fill="var(--card-black)"/>
          <rect x="6.5" y="4.5" width="5" height="3" fill="var(--card-black)"/>
        </svg>
        <span>(555) 472-9085</span>
      </div>
    </div>

    <div class="back-brand">
      <p class="brand-name brand-line-main">Meadowlark</p>
      <p class="brand-name brand-line-sub">Behavioral Partners, LLC</p>
    </div>
  </section>

</main>
</body>
</html>
```